Electrical needs letterhead design

Need a letterhead design for an electrical company. Using the same colours as to what are used in the logo.
After a modern design.

Want the logo in top right or top left.

Must include...

ABN 71 804 239 356
PHONE 0458203917
www.kelmaroo.com.au
jed@kelmaroo.com.au

'ABN' and 'PHONE' in bold.

Keep it basic. Logo top left, details either next to it or far right corner. Dont want any other objects included.

Electrical

```html
<!DOCTYPE html>
<html lang="en">
<head>
<meta charset="utf-8">
<title>Kelmaroo Electrical Services – Letterhead</title>
<link rel="stylesheet" href="https://fonts.googleapis.com/css2?family=Roboto:wght@400;500;700&display=swap">
<style>
  :root {
    --backdrop: #efefef;
    --paper: #ffffff;
    --brand-red: #9b1c1f;
    --band-edge: #7e1b1b;
    --band-mid: #d9432c;
    --ink: #2b2b2b;
    --ink-soft: #555555;
    --rule: #c9c9c9;
  }
  * { box-sizing: border-box; margin: 0; padding: 0; }
  html, body {
    width: 983px; height: 1200px; overflow: hidden;
    background: var(--backdrop);
    font-family: "Roboto", Arial, sans-serif;
  }
  .letterhead {
    position: absolute; left: 101px; top: 48px;
    width: 780px; height: 1103px;
    background: var(--paper);
    box-shadow: 0 1px 4px rgba(0,0,0,0.08);
  }
  .brand-name {
    position: absolute; left: 82px; top: 58px;
    font-size: 42px; font-weight: 500; color: var(--brand-red);
    letter-spacing: 0.5px; line-height: 1;
  }
  .contact-block {
    position: absolute; left: 516px; top: 64px;
    border-left: 1px solid var(--rule);
    padding-left: 20px; height: 82px;
  }
  .company-title {
    font-size: 12px; font-weight: 700; color: var(--ink);
    letter-spacing: 0.3px; margin-top: 4px; margin-bottom: 16px;
  }
  .contact-line {
    display: flex; align-items: center; gap: 7px;
    font-size: 11px; color: var(--ink-soft); line-height: 15px;
  }
  .contact-line.phone { font-size: 14px; font-weight: 700; color: var(--ink); margin-bottom: 2px; }
  .contact-line svg { width: 11px; height: 11px; fill: var(--ink-soft); flex: none; }
  .footer-shadow {
    position: absolute; left: 110px; width: 560px; top: 994px; height: 6px;
    background: radial-gradient(ellipse at center top, rgba(0,0,0,0.16), rgba(0,0,0,0) 70%);
  }
  .footer-details {
    position: absolute; left: 0; width: 100%; top: 1012px;
    text-align: center; font-size: 11px; color: var(--ink-soft);
  }
  .footer-details strong { color: var(--ink); font-weight: 700; }
  .footer-band {
    position: absolute; left: 0; bottom: 0; width: 100%; height: 57px;
    background: linear-gradient(90deg, var(--band-edge) 0%, #a8261f 30%, var(--band-mid) 55%, #a8261f 80%, var(--band-edge) 100%);
    border-top: 2px solid #5a1212;
  }
</style>
</head>
<body>
  <main class="letterhead">
    <div class="brand-name">Kelmaroo</div>

    <section class="contact-block">
      <p class="company-title">KELMAROO ELECTRICAL SERVICES</p>
      <p class="contact-line phone">
        <svg viewBox="0 0 12 12" aria-hidden="true"><path d="M3.5 0.5h5a1 1 0 0 1 1 1v9a1 1 0 0 1-1 1h-5a1 1 0 0 1-1-1v-9a1 1 0 0 1 1-1zm0.5 1.5v7h4v-7zm2 7.6a0.7 0.7 0 1 0 0.01 0z"/></svg>
        0458203917
      </p>
      <p class="contact-line email">
        <svg viewBox="0 0 12 12" aria-hidden="true"><path d="M1 2.5h10v7h-10zm1 1v0.4l4 2.6 4-2.6v-0.4zm0 1.6v3.4h8v-3.4l-4 2.6z"/></svg>
        jed@kelmaroo.com.au
      </p>
      <p class="contact-line web">
        <svg viewBox="0 0 12 12" aria-hidden="true"><circle cx="6" cy="6" r="5"/></svg>
        www.kelmaroo.com.au
      </p>
    </section>

    <div class="footer-shadow"></div>
    <p class="footer-details"><strong>ABN 71 804 239 356</strong> Brindle Park, Melbourne</p>
    <div class="footer-band"></div>
  </main>
</body>
</html>
```